Professional/modern business card design for construction company

We need a new business card design, double sided keeping it modern, sleek, professional and simple. We are an earthmoving business but do not want any pictures of machinery. I would like one side to have the logo and the other to have all the information, keeping with the colors in our logo. The business card will need to be able to be customised so we can use it for several different managers., we would also like to be able to use the design to apply it to other stationary ie. letterheads, notebooks etc. We do not really have a tag line but we could put on there that we specialise in - Agriculture, Civil Construction and Mining.

Contact Information for Business Card

Balgo Groundworks Pty Ltd
ABN 58 402 917 364
82 Dunmore Creek Road, Tarrawong NSW 2391

Desmond Fairweather
Managing Director
P 0438 614 205
E desfairweather@balgogroundworks.com.au

Font styles to use
Serif
Sans Serif

Requirements
Nice to have
• I have attached some examples of ideas.
Should not have
• images of machinery

```html
<!DOCTYPE html>
<html lang="en">
<head>
<meta charset="utf-8">
<title>Balgo Groundworks – Business Card</title>
<link rel="stylesheet" href="https://fonts.googleapis.com/css2?family=Roboto:wght@300;400;500;700&display=swap">
<style>
  :root {
    --charcoal: #3d3d3d;
    --charcoal-deep: #2f2f2f;
    --orange: #f28a1e;
    --white: #ffffff;
    --ink: #333333;
    --stage: #b9b9b9;
  }
  * { box-sizing: border-box; margin: 0; padding: 0; }
  html, body { width: 1200px; height: 930px; overflow: hidden; }
  body {
    background: var(--stage);
    font-family: "Roboto", sans-serif;
    position: relative;
  }
  .card {
    position: absolute;
    width: 560px;
    height: 340px;
    border-radius: 20px;
    overflow: hidden;
  }
  /* Front */
  .card-front {
    left: 80px; top: 90px;
    background: linear-gradient(135deg, #4a4a4a 0%, var(--charcoal) 60%, var(--charcoal-deep) 100%);
  }
  .front-brand {
    position: absolute;
    left: 0; right: 0; top: 50%;
    transform: translateY(-50%);
    display: flex; align-items: center; justify-content: center; gap: 14px;
  }
  .brand-mark {
    width: 18px; height: 18px; background: var(--orange); flex: none;
  }
  .brand-name {
    font-family: "Roboto", sans-serif;
    font-weight: 700;
    text-transform: uppercase;
    letter-spacing: 1px;
  }
  .card-front .brand-name { color: var(--white); font-size: 30px; }

  /* Back */
  .card-back {
    left: 560px; top: 470px;
    background: var(--white);
  }
  .back-swoosh { position: absolute; inset: 0; }
  .back-brand {
    position: absolute; left: 40px; top: 124px;
    display: flex; align-items: flex-start; gap: 10px;
  }
  .back-brand .brand-mark { margin-top: 4px; }
  .card-back .brand-name { color: var(--charcoal); font-size: 19px; line-height: 1.25; }
  .holder {
    position: absolute; right: 30px; top: 104px; text-align: right;
  }
  .holder-name {
    color: var(--orange); font-size: 20px; font-weight: 400;
    text-transform: uppercase; letter-spacing: .5px;
  }
  .holder-title { color: var(--ink); font-size: 13px; margin-top: 2px; }
  .divider-long {
    position: absolute; left: 34px; right: 30px; top: 190px;
    height: 1px; background: var(--orange);
  }
  .address {
    position: absolute; right: 30px; top: 208px; text-align: right;
    color: var(--ink); font-size: 13px; line-height: 1.35;
  }
  .abn {
    position: absolute; left: 34px; top: 206px;
    font-size: 14px; color: var(--ink);
  }
  .abn .label { color: var(--orange); }
  .divider-short {
    position: absolute; left: 34px; width: 190px; top: 232px;
    height: 1px; background: var(--orange);
  }
  .contacts {
    position: absolute; left: 34px; top: 244px;
    list-style: none; font-size: 13px; color: var(--ink);
  }
  .contacts li { display: flex; align-items: center; gap: 8px; line-height: 22px; }
  .contacts svg { width: 12px; height: 12px; flex: none; }
  .contacts .accent { color: var(--orange); }
</style>
</head>
<body>

  <section class="card card-front" aria-label="Card front">
    <div class="front-brand">
      <span class="brand-mark"></span>
      <span class="brand-name">Balgo Groundworks Pty Ltd</span>
    </div>
  </section>

  <section class="card card-back" aria-label="Card back">
    <svg class="back-swoosh" viewBox="0 0 560 340" preserveAspectRatio="none">
      <path d="M0 0 H560 V28 C470 40 360 62 250 70 C150 78 60 80 0 112 Z" fill="var(--charcoal)"/>
      <path d="M0 112 C60 80 150 78 250 70 C360 62 470 40 560 28 L560 36 C470 50 360 74 250 84 C150 92 60 100 0 136 Z" fill="var(--orange)"/>
      <path d="M0 136 C50 108 120 100 180 96 C110 108 50 130 20 160 L0 176 Z" fill="var(--charcoal)"/>
    </svg>

    <div class="back-brand">
      <span class="brand-mark"></span>
      <span class="brand-name">Balgo Groundworks<br>Pty Ltd</span>
    </div>

    <div class="holder">
      <p class="holder-name">Desmond Fairweather</p>
      <p class="holder-title">Managing Director</p>
    </div>

    <div class="divider-long"></div>

    <p class="address">82 Dunmore Creek Road,<br>Tarrawong NSW 2391</p>

    <p class="abn"><span class="label">ABN :</span> 58 402 917 364</p>
    <div class="divider-short"></div>

    <ul class="contacts">
      <li>
        <svg viewBox="0 0 24 24"><path fill="var(--orange)" d="M6.6 10.8a15 15 0 0 0 6.6 6.6l2.2-2.2a1 1 0 0 1 1-.25 11.4 11.4 0 0 0 3.6.57 1 1 0 0 1 1 1V20a1 1 0 0 1-1 1A17 17 0 0 1 3 4a1 1 0 0 1 1-1h3.5a1 1 0 0 1 1 1c0 1.250.2 2.45.57 3.57a1 1 0 0 1-.25 1z"/></svg>
        0438 614 205
      </li>
      <li>
        <svg viewBox="0 0 24 24"><rect x="2" y="5" width="20" height="14" rx="1" fill="none" stroke="var(--orange)" stroke-width="2"/><path d="M2 6l10 7 10-7" fill="none" stroke="var(--orange)" stroke-width="2"/></svg>
        desfairweather@balgogroundworks.com.au
      </li>
      <li>
        <svg viewBox="0 0 24 24"><circle cx="12" cy="12" r="10" fill="none" stroke="var(--orange)" stroke-width="2"/><path d="M2 12h20M12 2c3 3 3 17 0 20M12 2c-3 3-3 17 0 20" fill="none" stroke="var(--orange)" stroke-width="1.6"/></svg>
        <span>www.<span class="accent">balgogroundworksptyltd</span>.com</span>
      </li>
    </ul>
  </section>

</body>
</html>
```